Corwith Lodge website redesign

After 8 years of our current site, we're ready to upgrade our site design. We'd like to generally make it more modern and clean and build it on a CMS like joomla for easier future maintenance.

Our hotel is a family-owned bed and breakfast that competes against much larger hotel chains in Aspen with fancier rooms and larger pricetags. Our hotel is priced moderately and features tasteful, uniquely-design rooms.

We are looking for a website that will showcase the uniqueness of our rooms, the history of the Lodge, and the friendliness of our staff.

Here are some other hotel sites we like:

http://www.brackenfoldhouse.example/

http://www.tollerpeakhaus.example/

http://www.quarrowstay.example/

*********

Scope of Work - I'm looking for a design AND build. The website should be built out in Joomla as part of the final deliverable.
Updates

Current website: http://www.corwithlodge.example/

Explanation of what design + build means:

I am looking for not only the design of the site, but also for the homepage and one subpage to be built out as well. I do NOT need the entire site built - only for those two pages to be built and I will retrofit the remainder of the pages.

Target Market(s)

travellers evaluating hotels in Aspen, Colorado.

Industry/Entity Type

Hotel

Requirements
Must have
• Must, must, must be based on a joomla template. "Rotating" large main image as central position on homepage is a must (see example websites mentioned above).

Nice to have
• We have an existing online reservation system. It would be nice to evaluate placing a "widget" on the homepage that integrates to the online reservation page. Similar to that feature that the Bracken Fold website has at the foot of the main image on their homepage.

```html
<!DOCTYPE html>
<html lang="en">
<head>
<meta charset="utf-8">
<title>Corwith Lodge — Welcome Home</title>
<link href="https://fonts.googleapis.com/css2?family=Arimo:wght@400;700&family=Open+Sans:wght@400;600;700&display=swap" rel="stylesheet">
<style>
  :root {
    --wood: #5a3a22;
    --wood-dark: #3f2613;
    --wood-line: rgba(30, 16, 6, 0.55);
    --brand: #6e2a1a;
    --brand-mid: #8e3b2a;
    --brand-light: #b9715f;
    --panel: #ffffff;
    --nav-bg: #f4f4f4;
    --nav-line: #dcdcdc;
    --text: #8c8c8c;
    --text-dark: #555555;
    --heading-gray: #5e5e5e;
    --accent-green: #4caf50;
    --tick: #5cc83c;
    --white: #ffffff;
  }
  * { box-sizing: border-box; margin: 0; padding: 0; }
  html, body { width: 1015px; height: 1200px; overflow: hidden; }
  body {
    position: relative;
    font-family: "Arimo", Arial, sans-serif;
    background-color: var(--wood);
    background-image:
      repeating-linear-gradient(90deg, transparent 0 64px, var(--wood-line) 64px 66px),
      linear-gradient(180deg, #5e3c23 0%, var(--wood-dark) 100%);
  }
  a { color: inherit; text-decoration: none; }

  .top-bar { position: absolute; top: 9px; left: 110px; width: 797px; font-size: 11px; font-weight: 700; color: var(--white); }
  .top-bar .phone { position: absolute; left: 0; }
  .top-bar .account { position: absolute; right: 0; display: flex; gap: 10px; }

  .site-header { position: absolute; top: 32px; left: 110px; width: 797px; height: 75px; background: var(--nav-bg); box-shadow: 0 1px 3px rgba(0,0,0,.4); }
  .brand { position: absolute; left: 0; top: 0; width: 121px; height: 75px;
    background: radial-gradient(ellipse at 70% 40%, var(--brand-light) 0%, var(--brand-mid) 45%, var(--brand) 100%);
    display: flex; align-items: center; justify-content: center;
    font-family: "Open Sans", sans-serif; font-size: 13px; font-weight: 600; color: var(--white); }
  .main-nav { position: absolute; left: 121px; top: 0; right: 0; height: 41px; display: flex; border-bottom: 1px solid var(--nav-line); background: linear-gradient(#fbfbfb, #ececec); }
  .main-nav a { display: flex; align-items: center; justify-content: center; font-size: 10.5px; font-weight: 700; color: #444; border-right: 1px solid var(--nav-line); }
  .main-nav a:last-child { border-right: 0; }
  .main-nav a.current { color: var(--brand-mid); background: #fff; }
  .sub-nav { position: absolute; left: 121px; top: 41px; right: 0; height: 34px; display: flex; align-items: center; }
  .sub-nav a { font-size: 10px; font-weight: 700; color: #8a8a8a; margin-left: 19px; margin-right: 14px; }
  .search { position: absolute; right: 13px; top: 5px; width: 146px; height: 21px; border: 1px solid #ccc; background: #fff; box-shadow: inset 0 1px 2px rgba(0,0,0,.15); font-size: 8px; color: #999; padding: 5px 5px; font-family: "Arimo", sans-serif; }

  .hero { position: absolute; top: 116px; left: 110px; width: 795px; height: 376px;
    background: linear-gradient(160deg, #6b3d22 0%, #8a4a2c 30%, #a4392f 45%, #c89a86 65%, #8c5c3a 85%, #e7c9a8 100%); }
  .hero-caption { position: absolute; left: 296px; top: 309px; width: 476px; height: 50px; background: rgba(240,240,240,.95);
    font-family: "Arimo", sans-serif; font-weight: 700; font-size: 26px; color: #8a8a8a; padding: 12px 24px; }

  .content { position: absolute; top: 504px; left: 110px; width: 794px; height: 592px; background: var(--panel); border-bottom: 3px solid var(--brand); }
  .welcome-title { position: absolute; left: 34px; top: 30px; font-family: "Open Sans", sans-serif; font-weight: 700; font-size: 20px; color: var(--brand); letter-spacing: .5px; }
  .welcome-text { position: absolute; left: 34px; top: 75px; width: 254px; font-family: "Open Sans", sans-serif; font-size: 10.5px; line-height: 18.6px; color: var(--text); }
  .badge { position: absolute; }
  .badge.certificate { left: 29px; top: 429px; width: 127px; height: 103px; border: 1px solid #bbb; border-bottom: 16px solid #5aa844; background: #fff; }
  .badge.ranking { left: 198px; top: 402px; width: 86px; height: 135px; border: 1px solid #bbb; border-bottom: 12px solid var(--brand-mid); background: linear-gradient(#fff, #b6dba0); }
  .badge.ranking::after { content: ""; position: absolute; left: 11px; top: 10px; width: 62px; height: 62px; border-radius: 50%; background: #8cc46d; }

  .offers-title { position: absolute; left: 338px; top: 32px; font-family: "Open Sans", sans-serif; font-weight: 700; font-size: 20px; color: var(--heading-gray); letter-spacing: .5px; }
  .slider-dots { position: absolute; left: 742px; top: 43px; display: flex; gap: 5px; }
  .slider-dots span { width: 8px; height: 8px; border-radius: 50%; background: #ccc; }
  .slider-dots span.active { background: var(--accent-green); }

  .offer { position: absolute; width: 137px; height: 173px; border: 1px solid #e4e4e4; background: #fff; }
  .offer .thumb { position: absolute; left: 18px; top: 12px; width: 102px; height: 85px; }
  .offer .caption { position: absolute; left: 18px; top: 103px; width: 104px; font-family: "Open Sans", sans-serif; font-size: 8.5px; line-height: 10px; color: var(--text-dark); }
  .offer .price { position: absolute; right: 17px; top: 124px; font-family: "Open Sans", sans-serif; font-size: 9px; font-weight: 700; color: var(--brand); }
  .offer .buy { position: absolute; left: 60px; top: 144px; width: 61px; height: 19px; background: linear-gradient(#6a6a6a, #3c3c3c); border-right: 3px solid var(--brand-mid); color: #fff; font-family: "Open Sans", sans-serif; font-size: 9px; font-weight: 700; display: flex; align-items: center; justify-content: center; letter-spacing: .3px; }
  .thumb.peak { background: linear-gradient(#b9bcbc 0%, #6c706c 45%, #8aa040 75%, #c8a030 100%); }
  .thumb.room { background: linear-gradient(160deg, #5c3520, #a83a33 40%, #d4b0a2 70%, #6a4a30); }
  .thumb.plaque { background: radial-gradient(ellipse at 50% 45%, #c8894a 0%, #7a4318 55%, #2a140a 100%); }
  .thumb.lodge { background: linear-gradient(#dde1e8 0%, #a7adb5 30%, #7a5236 60%, #c4c0b8 100%); }

  .reserve-banner { position: absolute; left: 338px; top: 466px; width: 436px; height: 76px; }
  .reserve-banner .shadow { position: absolute; left: 5px; top: 5px; right: -5px; bottom: -5px; background: #5a1f14; }
  .reserve-banner .face { position: absolute; inset: 0; background: linear-gradient(90deg, #6d2a1c 0%, #944434 50%, #7a3222 100%); display: flex; align-items: center; }
  .reserve-banner svg { margin-left: 45px; }
  .reserve-banner .label { margin-left: 42px; font-family: "Open Sans", sans-serif; font-weight: 700; color: #fff; line-height: 21px; text-shadow: 1px 1px 2px rgba(0,0,0,.4); }
  .reserve-banner .label .big { font-size: 26px; }
  .reserve-banner .label .small { font-size: 19px; }
  .reserve-banner .label .line2 { font-size: 24px; display: block; }

  .site-footer { position: absolute; top: 1117px; left: 113px; font-size: 10.5px; color: #fff; }
  .site-footer a { position: absolute; white-space: nowrap; }
</style>
</head>
<body>
  <div class="top-bar">
    <span class="phone">Reservation: 5550 5550 55500</span>
    <span class="account"><a href="#">Login</a><a href="#">Register</a></span>
  </div>

  <header class="site-header">
    <a class="brand" href="#">Corwith Lodge</a>
    <nav class="main-nav">
      <a class="current" href="#" style="width:69px">Home</a>
      <a href="#" style="width:98px">About</a>
      <a href="#" style="width:104px">Rooms</a>
      <a href="#" style="width:151px">Manager’s Journal</a>
      <a href="#" style="width:127px">Reservations</a>
      <a href="#" style="width:127px">Contact</a>
    </nav>
    <nav class="sub-nav">
      <a href="#">Amenities</a>
      <a href="#">Aspen Information</a>
      <a href="#">Webcams</a>
      <div class="search">search...</div>
    </nav>
  </header>

  <section class="hero" role="img" aria-label="Rotating photo: guest room with a patchwork quilt, red pillows and a carved wooden nightstand">
    <div class="hero-caption">WELCOME HOME</div>
  </section>

  <main class="content">
    <h2 class="welcome-title">WELCOME</h2>
    <p class="welcome-text">Located in the heart of downtown Aspen, the newly renovated Corwith Lodge possesses all the charms of a vintage European Ski Lodge, while offering all of the modern conveniences one would expect with a stay in Aspen.<br>A stay at our lodge includes free continental breakfast in our dining room, daily maid service, free wireless internet access, and a fully-equipped conference facility. Guests are also invited to relax in one of our two outdoor Jacuzzis or in our lounge, where a 42-inch plasma TV and fireplace make for a pleasant area to unwind.</p>
    <div class="badge certificate" role="img" aria-label="Certificate of excellence badge"></div>
    <div class="badge ranking" role="img" aria-label="Travel review ranking badge"></div>

    <h2 class="offers-title">OUR OFFERS</h2>
    <div class="slider-dots"><span class="active"></span><span></span><span></span></div>

    <div class="offer" style="left:338px;top:79px"><div class="thumb peak" role="img" aria-label="Misty mountain with autumn aspens"></div><p class="caption">3 nights after Christ-<br>mas in Aspen!</p><span class="price">$ 300</span><a class="buy" href="#">Buy now!</a></div>
    <div class="offer" style="left:490px;top:79px"><div class="thumb room" role="img" aria-label="Guest room bed"></div><p class="caption">3 nights after Christ-<br>mas in Aspen!</p><span class="price">$ 300</span><a class="buy" href="#">Buy now!</a></div>
    <div class="offer" style="left:642px;top:79px"><div class="thumb plaque" role="img" aria-label="Carved wooden lodge sign"></div><p class="caption">3 nights after Christ-<br>mas in Aspen!</p><span class="price">$ 300</span><a class="buy" href="#">Buy now!</a></div>
    <div class="offer" style="left:338px;top:268px"><div class="thumb lodge" role="img" aria-label="Lodge exterior in winter"></div><p class="caption">3 nights after Christ-<br>mas in Aspen!</p><span class="price">$ 300</span><a class="buy" href="#">Buy now!</a></div>
    <div class="offer" style="left:490px;top:268px"><div class="thumb plaque" role="img" aria-label="Carved wooden lodge sign"></div><p class="caption">3 nights after Christ-<br>mas in Aspen!</p><span class="price">$ 300</span><a class="buy" href="#">Buy now!</a></div>
    <div class="offer" style="left:642px;top:268px"><div class="thumb plaque" role="img" aria-label="Carved wooden lodge sign"></div><p class="caption">3 nights after Christ-<br>mas in Aspen!</p><span class="price">$ 300</span><a class="buy" href="#">Buy now!</a></div>

    <a class="reserve-banner" href="#">
      <span class="shadow"></span>
      <span class="face">
        <svg width="56" height="56" viewBox="0 0 56 56" aria-hidden="true"><path d="M4 30 L20 46 L52 6 L48 4 L20 36 L10 24 Z" fill="var(--tick)"/></svg>
        <span class="label"><span class="big">Check</span> <span class="small">our</span><span class="line2">reservation system</span></span>
      </span>
    </a>
  </main>

  <footer class="site-footer">
    <a href="#" style="left:0">Home</a>
    <a href="#" style="left:77px">About</a>
    <a href="#" style="left:152px">Rooms</a>
    <a href="#" style="left:219px">Manager’s Journal</a>
    <a href="#" style="left:340px">Reservations</a>
    <a href="#" style="left:433px">Contact</a>
  </footer>
</body>
</html>
```